依頼詳細
①去年のチラシデータを添付させていただきました。
②今年はコンクールが中止となったため、写真は昨年の中央の時の写真と、アンサンブルコンテスト支部大会の写真を入れていただきたいです。
③部活のロゴがあるので、それもどこかに入れていただきたいです。
④観客は保護者のみなので、場所の地図は不要です。
⑤公式VIDORAチャンネルのQRコードはどこかに入れてほしいです。
⑥ここ数年緑や茶色などが多かったので、ピンク、赤、青などの色で作ってみたいです。イメージは特にありません。あまりに子供っぽいものは好きではないです。

・今回のデータをDVDジャケットに転用させていただきますのでよろしくお願い申し上げます。

よろしくお願い致します。
記載項目
札幌市立柳浦中学校吹奏楽部
第12回定期演奏会
【無観客演奏会~保護者、関係者のみ人数を制限して入場しています。】
11月1日(日)13:00開場 13:30開演 15:00終演予定
場所:ヒバリノ会館(札幌紅葉アリーナ)
主催:札幌市立柳浦中学校 吹奏楽部保護者会
●プログラム

〇第43回中央室内楽フェスタ演奏予定曲
「砂丘の鐘と港の夜明け」~木管8重奏バージョン~Tovelu作曲
〇ウィンディ・ハーバー「舟と小夜子の夢渡り」より
〇ボルディエット
〇元気200km
〇サクソフォンとバンドのための夏空の約束~ミルバーンズ 永遠のレパートリーより~
〇風を追って走ろうよ in swing
ほか

☆VIDORA無料ライブ配信~札幌市立柳浦中学校吹奏楽部公式チャンネルにて!
☆お問い合わせ 札幌市立柳浦中学校 鹿間・楢戸・砂川(011-555-0178)
☆今回の定期演奏会は、新型コロナウイルス感染予防防止の観点から、保護者・学校関係者のみの公演となりました。

サイズ
A4
ページ数
片面
希望イメージ
シンプル 複雑
単色 カラフル
暗い 明るい
日常 高級
遊び心 厳粛
未来的 伝統的
女性的 男性的
希望する色
赤系、青系
納品ファイル
• 高解像度JPG (.jpg)
• PNG形式 (.png)
補足説明
ファイルはよくわからないのですが、プリモスなどの印刷会社に200枚程度の印刷をお願いするのと、Chirpzaやホームページにチラシ画像を貼る予定です。どのファイル形式がよいかは教えてください。
Vidoraでのライブ配信の部分が目立つようにしてほしいです。今回は一般の方に会場に来ていただくことはできないので、Vidoraを出来るだけたくさんの方に見ていただきたいです。

ライブ配信をした、他のバンドのチラシを添付します。

デザインがとても素敵だったのと
VIDDORAへの誘導が必要だったので
手に持ったスマホのデザインがとても気に入りました。

今回はたくさんの提案ありがとうございました。
こんな制度を知らなかったので、ぜひ今後とも利用しようと思いました。

```html
<!DOCTYPE html>
<html lang="ja">
<head>
<meta charset="utf-8">
<title>柳浦中学校吹奏楽部 第12回定期演奏会</title>
<link href="https://fonts.googleapis.com/css2?family=Noto+Sans+JP:wght@400;500;700;900&family=Noto+Serif+JP:wght@600;700;900&family=Oswald:wght@500;600&display=swap" rel="stylesheet">
<style>
  :root {
    --red: #c8192f;
    --navy: #1e2a58;
    --navy-soft: #3a4676;
    --cream: #f7f1ea;
    --paper: #fbf8f4;
    --gold: #ffe27a;
    --ink: #2a2a33;
  }
  * { margin: 0; padding: 0; box-sizing: border-box; }
  html, body { width: 847px; height: 1200px; overflow: hidden; background: var(--paper); }
  .flyer {
    position: relative; width: 847px; height: 1200px; overflow: hidden;
    background: linear-gradient(180deg, var(--paper) 0%, var(--cream) 100%);
    font-family: "Noto Sans JP", sans-serif; color: var(--ink);
  }
  .stream-band {
    position: absolute; left: 0; top: 0; width: 100%; height: 92px;
    background: var(--red); display: flex; align-items: center; padding: 0 36px; gap: 22px;
  }
  .stream-brand { display: flex; align-items: center; gap: 8px; font-weight: 700; font-size: 30px; color: #fff; }
  .stream-brand .mark { width: 22px; height: 22px; background: #fff; }
  .stream-copy { text-align: center; flex: 1; }
  .stream-title { font-family: "Noto Serif JP", serif; font-weight: 900; font-size: 40px; color: var(--gold); line-height: 1.1; letter-spacing: 1px; }
  .stream-sub { font-size: 17px; font-weight: 700; color: #fff; margin-top: 4px; }

  .ornament { position: absolute; background: radial-gradient(circle, var(--navy-soft) 0%, rgba(58,70,118,0.15) 70%, transparent 72%); }
  .ornament.top { right: 60px; top: 170px; width: 70px; height: 70px; }
  .ornament.left { left: 40px; top: 470px; width: 80px; height: 70px; }

  .heading { position: absolute; left: 0; top: 250px; width: 100%; text-align: center; color: var(--navy); }
  .heading .club { font-family: "Noto Serif JP", serif; font-weight: 700; font-size: 32px; letter-spacing: 2px; }
  .heading .concert { font-family: "Noto Serif JP", serif; font-weight: 900; font-size: 70px; letter-spacing: 4px; line-height: 1.2; }
  .heading .rule { width: 580px; height: 2px; background: var(--navy); margin: 6px auto 0; }

  .notice { position: absolute; left: 0; top: 440px; width: 100%; text-align: center; font-size: 16px; font-weight: 500; line-height: 1.8; color: var(--navy); }

  .photo { position: absolute; background: linear-gradient(180deg, #5a4a46 0%, #8d7a70 45%, #3c3436 100%); }
  .photo.main { left: 0; top: 520px; width: 847px; height: 200px; }
  .photo.group { left: 622px; top: 790px; width: 195px; height: 88px; background: linear-gradient(180deg, #b8b0a8, #6d6670); }
  .photo.ensemble { left: 622px; top: 905px; width: 195px; height: 108px; background: linear-gradient(180deg, #e4dcd4, #9b8f88); }

  .date { position: absolute; left: 56px; top: 724px; color: var(--red); }
  .date .year { display: block; font-family: "Oswald", sans-serif; font-weight: 600; font-size: 40px; line-height: 1; }
  .date .row { display: flex; align-items: flex-end; gap: 10px; }
  .date .day { font-family: "Oswald", sans-serif; font-weight: 600; font-size: 100px; line-height: 1; }
  .date .weekday { width: 52px; height: 52px; border-radius: 50%; border: 3px solid var(--red); display: flex; align-items: center; justify-content: center; font-weight: 900; font-size: 26px; margin-bottom: 8px; }

  .times { position: absolute; left: 420px; top: 755px; width: 185px; border-left: 3px solid var(--red); padding-left: 14px; }
  .times p { font-size: 21px; font-weight: 700; color: var(--navy); line-height: 1.5; }
  .venue { position: absolute; left: 56px; top: 860px; font-size: 16px; font-weight: 700; color: var(--navy); }

  .program { position: absolute; left: 30px; top: 893px; width: 565px; height: 180px; border: 2px solid var(--navy); background: rgba(255,255,255,0.7); }
  .program h2 { background: var(--navy); color: #fff; font-size: 15px; font-weight: 700; padding: 3px 12px; letter-spacing: 2px; }
  .program ul { list-style: none; padding: 8px 12px; font-size: 12.5px; line-height: 1.65; color: var(--ink); }
  .program .note { padding-left: 1em; font-size: 11.5px; }

  .footer { position: absolute; left: 30px; top: 1092px; width: 680px; height: 80px; display: flex; align-items: center; gap: 24px; }
  .club-name { display: flex; align-items: center; gap: 8px; font-family: "Noto Serif JP", serif; font-weight: 700; font-size: 17px; color: var(--navy); width: 240px; line-height: 1.2; }
  .club-name .dot { width: 22px; height: 22px; border-radius: 50%; background: var(--navy); flex: none; }
  .contact { font-size: 14px; font-weight: 500; color: var(--navy); line-height: 1.5; }
  .contact .host { font-size: 12px; }
  .qr-code { position: absolute; left: 730px; top: 1092px; width: 82px; height: 82px; background: #fff; border: 2px solid var(--navy); }
  .base-band { position: absolute; left: 0; bottom: 0; width: 100%; height: 16px; background: var(--navy); }
  .base-band::before { content: ""; position: absolute; left: 0; top: -6px; width: 100%; height: 4px; background: var(--red); }
</style>
</head>
<body>
<div class="flyer">
  <header class="stream-band">
    <div class="stream-brand"><span class="mark"></span>Vidora</div>
    <div class="stream-copy">
      <p class="stream-title">VIDORA無料ライブ配信!</p>
      <p class="stream-sub">札幌市立柳浦中学校吹奏楽部公式チャンネルにて開催!</p>
    </div>
  </header>

  <div class="ornament top" role="img" aria-label="紺色の蝶の装飾"></div>
  <div class="ornament left" role="img" aria-label="紺色の蝶の装飾"></div>

  <section class="heading">
    <p class="club">札幌市立柳浦中学校吹奏楽部</p>
    <h1 class="concert">第12回定期演奏会</h1>
    <div class="rule"></div>
  </section>

  <p class="notice">今回の定期演奏会は、新型コロナウイルス感染予防防止の観点から、<br>保護者・学校関係者のみの公演となりました。</p>

  <div class="photo main" role="img" aria-label="ホールのステージで演奏する吹奏楽部の写真"></div>

  <div class="date">
    <span class="year">2020</span>
    <div class="row">
      <span class="day">11.1</span>
      <span class="weekday">日</span>
    </div>
  </div>
  <div class="times">
    <p>13:00開場</p>
    <p>13:30開演</p>
    <p>15:00終演予定</p>
  </div>
  <div class="photo group" role="img" aria-label="ステージ上の部員集合写真"></div>
  <div class="photo ensemble" role="img" aria-label="アンサンブル大会の演奏写真"></div>
  <p class="venue">場所:ヒバリノ会館(札幌紅葉アリーナ)</p>

  <section class="program">
    <h2>プログラム</h2>
    <ul>
      <li>〇第43回中央室内楽フェスタ演奏予定曲</li>
      <li class="note">「砂丘の鐘と港の夜明け」~木管8重奏バージョン~Tovelu作曲</li>
      <li>〇ウィンディ・ハーバー「舟と小夜子の夢渡り」より</li>
      <li>〇ボルディエット 〇元気200km</li>
      <li>〇サクソフォンとバンドのための夏空の約束~ミルバーンズ 永遠のレパートリーより~</li>
      <li>〇風を追って走ろうよ in swing ほか</li>
    </ul>
  </section>

  <footer class="footer">
    <div class="club-name"><span class="dot"></span>YANAGIURA WIND ORCHESTRA</div>
    <div class="contact">
      <p>お問い合わせ:</p>
      <p>札幌市立柳浦中学校 鹿間・楢戸・砂川(011-555-0178)</p>
      <p class="host">主催:札幌市立柳浦中学校 吹奏楽部保護者会</p>
    </div>
  </footer>
  <div class="qr-code" role="img" aria-label="公式Vidoraチャンネルへのコードを置く場所"></div>
  <div class="base-band"></div>
</div>
</body>
</html>
```